Veterinary Anesthesia Machine Stickers

We want to use the machine pictures below but make it more appealing for stickers and not so "life like". With our name TL Medical somewhere under it. On the larger anesthesia machine screen we want to say:
you're a reservoir of knowledge.
Similar to the example, but with a different machine.

For the smaller anesthesia machine (novra-3-8) we want our name under it somewhere and the same type of look as the larger machine. But we want this one to say:
Just breathe

Veterinarians and veterinary technicains

```html
<!DOCTYPE html>
<html lang="en">
<head>
<meta charset="utf-8">
<title>TL Medical – Just Breathe sticker</title>
<link rel="stylesheet" href="https://fonts.googleapis.com/css2?family=Russo+One&family=Lato:wght@400&display=swap">
<style>
  :root {
    --page: #ffffff;
    --cream: #fdf8e4;
    --cream-light: #fffdf6;
    --bronze: #8e5e3a;
    --gold: #e8b865;
    --sand: #f1d39c;
    --teal: #5ec4b9;
    --ink: #2a5a73;
    --logo-ink: #234f63;
    --machine-white: #eef0f1;
    --machine-grey: #c9cfd3;
  }
  html, body {
    margin: 0;
    padding: 0;
    width: 1147px;
    height: 1200px;
    overflow: hidden;
    background: var(--page);
  }
  .sticker {
    position: absolute;
    left: 0;
    top: 26px;
    width: 1147px;
    height: 1147px;
  }
  .headline {
    font-family: "Russo One", "Arial Black", sans-serif;
    font-size: 118px;
    fill: var(--ink);
    letter-spacing: -2px;
  }
  .brand-name {
    font-family: "Lato", Arial, sans-serif;
    font-size: 64px;
    font-weight: 400;
    fill: var(--logo-ink);
  }
</style>
</head>
<body>
  <svg class="sticker" viewBox="0 0 1480 1480" xmlns="http://www.w3.org/2000/svg">
    <defs>
      <linearGradient id="frameWarm" x1="0" y1="0" x2="1" y2="0">
        <stop offset="0" stop-color="var(--bronze)"/>
        <stop offset="0.65" stop-color="var(--gold)"/>
        <stop offset="1" stop-color="var(--sand)"/>
      </linearGradient>
      <radialGradient id="panelGlow" cx="0.55" cy="0.5" r="0.7">
        <stop offset="0" stop-color="var(--cream-light)"/>
        <stop offset="1" stop-color="var(--cream)"/>
      </radialGradient>
      <linearGradient id="machineTone" x1="0" y1="0" x2="1" y2="1">
        <stop offset="0" stop-color="var(--machine-white)"/>
        <stop offset="1" stop-color="var(--machine-grey)"/>
      </linearGradient>
    </defs>

    <rect class="panel" x="60" y="60" width="1360" height="1360" rx="70" fill="url(#panelGlow)"/>

    <path class="frame-warm" d="M51,150 V126 A75,75 0 0 1 126,51 H1355 A75,75 0 0 1 1430,126 V1020"
          fill="none" stroke="url(#frameWarm)" stroke-width="30" stroke-linecap="round"/>
    <path class="frame-teal" d="M51,345 V1355 A75,75 0 0 0 126,1430 H1355 A75,75 0 0 0 1430,1355 V1205"
          fill="none" stroke="var(--teal)" stroke-width="30" stroke-linecap="round"/>

    <rect class="machine-art" x="250" y="222" width="485" height="1050" rx="40"
          fill="url(#machineTone)" opacity="0.85"
          role="img" aria-label="Illustration of the novra-3-8 veterinary anesthesia machine on a wheeled stand with screen, flowmeter, vaporizer and breathing hoses"/>

    <g class="headline-group" transform="skewX(-14)">
      <text class="headline" x="840" y="563">JUST</text>
      <text class="headline" x="856" y="668">BREATHE</text>
    </g>

    <g class="brand">
      <rect class="brand-mark" x="930" y="1150" width="40" height="40" fill="var(--logo-ink)"/>
      <text class="brand-name" x="990" y="1193">TL Medical</text>
    </g>
  </svg>
</body>
</html>
```